Website Design For Needlecraftparcel.com

What: A range of Tapestry Kits, books & Accessories.
Who: Appeals to ladies 45-70 years.

What we need:
A home page and template for a product page
The home page needs to include the image and something we can use as a logo to get started.

Image:
I love the 'Marla Whitcombe' feel, hearts, flags and bunting.
Tapestry tends to be rich, heavy fabrics so dark burgendy reds and navy blues might work quite well in moderation.

Layout:
I would like the core structure of the site to be similar to:
http://www.fernquills.example (although this is just a suggestion feel free to try something else if you think it might work better.
Buttons along the top: Home, About Tapestry, Delivery, Contact Us (the drop down on Our Range is Tapestry Cushions.

I would also like the search box to be a little bigger and can be relocated.

Tabs under the image
Cushion Kits, Hanging Tapestrys, Books, Accessories, Advice
Then an area for featured products under that.

Images - You can use any of the images from The Olden Stitchwork Guild - tapestry section to build a feel for how the site might look when populated with product.

Female 45-75yrs -

It Company

• Build with SEO in mind.
Some space for text on home page for seo
Some images below to give a feel for styling

```html
<!DOCTYPE html>
<html lang="en">
<head>
<meta charset="utf-8">
<title>Needlecraftparcel – Tapestry Kits, Books &amp; Accessories</title>
<link rel="stylesheet" href="https://fonts.googleapis.com/css2?family=Open+Sans:wght@400;600&display=swap">
<style>
  :root {
    --navy: #1f2370;
    --slate: #3f5a6c;
    --burgundy: #7a0d2b;
    --red: #9b1111;
    --velvet: #a3122a;
    --velvet-dark: #6e0f1f;
    --frame: #3a3a3a;
    --hero-grey: #ebebeb;
    --search-grey: #9d9d9d;
    --button-grey: #dcdcdc;
    --text: #3a4a58;
    --white: #ffffff;
    --ink: #111111;
  }
  * { box-sizing: border-box; margin: 0; padding: 0; }
  html, body { width: 1200px; height: 900px; overflow: hidden; background: var(--white); }
  body { font-family: "Open Sans", Verdana, sans-serif; color: var(--text); position: relative; }

  .site {
    position: absolute; left: 195px; top: 45px; width: 855px; height: 804px;
    border: 2px solid var(--ink); background: var(--white);
    box-shadow: 3px 4px 6px rgba(0,0,0,0.35);
  }
  .site > * { position: absolute; }

  .brand { left: 18px; top: 52px; display: flex; align-items: center; gap: 10px; }
  .brand-dot { width: 18px; height: 18px; border-radius: 50%; background: var(--red); }
  .brand-name { font-size: 34px; font-weight: 400; color: var(--navy); letter-spacing: 0.2px; }
  .phone { right: 18px; top: 59px; font-size: 17px; color: var(--red); letter-spacing: 0.4px; }

  .main-nav { left: 163px; top: 106px; width: 688px; height: 49px; background: var(--slate); }
  .main-nav a { position: absolute; top: 0; line-height: 49px; font-size: 13.5px; color: var(--white); text-decoration: none; }
  .main-nav a.active { left: 3px; width: 87px; background: var(--red); text-align: center; }

  .welcome {
    left: 0; top: 108px; width: 160px; height: 425px; background: var(--white);
    box-shadow: 3px 3px 5px rgba(0,0,0,0.4); z-index: 2; padding-top: 17px;
  }
  .welcome h1 { font-size: 13.5px; font-weight: 400; text-align: center; line-height: 20px; color: var(--slate); }
  .welcome p { margin: 9px 0 0 31px; width: 112px; font-size: 9.6px; line-height: 17.9px; color: var(--text); }
  .social { position: absolute; left: 23px; top: 365px; display: flex; gap: 14px; }
  .social span { width: 25px; height: 25px; border-radius: 4px; display: block; }
  .social .s1 { background: #3b5998; }
  .social .s2 { background: #5bb4d6; }
  .social .s3 { background: #1d6fa5; }

  .hero { left: 161px; top: 155px; width: 690px; height: 315px; background: var(--hero-grey); }
  .hero-photo {
    position: absolute; left: 128px; top: 24px; width: 412px; height: 282px;
    border-radius: 6px;
    background: linear-gradient(180deg, var(--velvet) 0%, var(--velvet-dark) 62%, var(--frame) 100%);
  }

  .category-nav { left: 161px; top: 470px; width: 690px; height: 66px; background: var(--slate); }
  .category-nav a { position: absolute; top: 0; line-height: 66px; font-size: 13.5px; color: var(--white); text-decoration: none; }

  .featured { left: 0; top: 536px; width: 851px; height: 239px; background: var(--burgundy); }
  .featured-bar { position: absolute; left: 2px; top: 14px; width: 847px; height: 41px; background: var(--slate); }
  .featured-bar h2 { position: absolute; left: 38px; top: 4px; font-size: 22px; font-weight: 400; color: var(--white); }
  .search { position: absolute; left: 592px; top: 5px; width: 250px; height: 31px; background: var(--search-grey); }
  .search-field { position: absolute; left: 6px; top: 5px; width: 178px; height: 21px; background: var(--white); border: 0; }
  .search-button {
    position: absolute; left: 186px; top: 3px; width: 62px; height: 25px; background: var(--button-grey);
    border: 0; font: 400 9px/10px "Open Sans", Verdana, sans-serif; color: var(--ink);
  }

  .product { position: absolute; top: 63px; height: 176px; background: var(--white); }
  .product p { margin: 7px 0 0 16px; font-size: 8px; line-height: 14px; color: var(--text); }
  .product-photo { position: absolute; left: 19px; top: 81px; width: 94px; height: 82px; border: 2px solid #b5b5b5; }
  .best-seller { position: absolute; left: 60px; top: 48px; width: 60px; text-align: center; font-size: 8px; color: var(--red); }
  .best-seller svg { display: block; margin: 0 auto 2px; }

  .footer { left: 0; top: 775px; width: 851px; height: 25px; background: var(--slate); color: var(--white);
    font-size: 11px; line-height: 25px; text-align: center; }
</style>
</head>
<body>
<div class="site">
  <header class="brand">
    <span class="brand-dot"></span>
    <span class="brand-name">Needlecraftparcel</span>
  </header>
  <div class="phone">5550 1234 0199</div>

  <nav class="main-nav">
    <a class="active" href="#">Home</a>
    <a style="left:114px" href="#">About Tapestry</a>
    <a style="left:252px" href="#">Delivery</a>
    <a style="left:349px" href="#">Contact Us</a>
    <a style="left:460px" href="#">Our Range in Tapestry Cushions</a>
  </nav>

  <aside class="welcome">
    <h1>Welcome to<br>Needlecraftparcel</h1>
    <p>Praesent accumsan bibendum risus fring-illa tincidunt. Cum sociis natoque penati-bus et magnis dis parturient montes, nascetur ridiculus musnec sollicitudin vulputate felis. Curabitur malesuada dictum cursus. Ut porttitor ipsum vel elit ultrices viverra. Sed ullamcorper elit eget leo ultricies gravida.</p>
    <div class="social"><span class="s1"></span><span class="s2"></span><span class="s3"></span></div>
  </aside>

  <section class="hero">
    <div class="hero-photo" role="img" aria-label="Red velvet bench with tapestry cushions and a teddy bear"></div>
  </section>

  <nav class="category-nav">
    <a style="left:37px" href="#">Cushion Kits</a>
    <a style="left:178px" href="#">Hanging Tapestry</a>
    <a style="left:350px" href="#">Books</a>
    <a style="left:457px" href="#">Accessories</a>
    <a style="left:591px" href="#">Advice</a>
  </nav>

  <section class="featured">
    <div class="featured-bar">
      <h2>Featured Products</h2>
      <form class="search">
        <input class="search-field" type="text" aria-label="Search products">
        <button class="search-button" type="button">PRODUCT SEARCH</button>
      </form>
    </div>

    <article class="product" style="left:2px;width:136px">
      <p>orem ipsum dolor sit<br>amet, consectetur<br>adipiscing elit. Sed<br>$45.00</p>
      <div class="product-photo" role="img" aria-label="Owl tapestry cushion with pompom trim" style="background:linear-gradient(135deg,#e9e2d4,#b08a5a)"></div>
    </article>
    <article class="product" style="left:142px;width:136px">
      <p>orem ipsum dolor sit<br>amet, consectetur<br>adipiscing elit. Sed<br>$45.00</p>
      <div class="product-photo" role="img" aria-label="Union flag keep calm tapestry cushion" style="background:linear-gradient(135deg,#b7c0cc,#8a3a3e)"></div>
    </article>
    <article class="product" style="left:282px;width:135px">
      <p>orem ipsum dolor sit<br>amet, consectetur<br>adipiscing elit. Sed<br>$45.00</p>
      <div class="product-photo" role="img" aria-label="Love lettered striped tapestry cushion" style="background:linear-gradient(135deg,#ece6e0,#c59a8a)"></div>
    </article>
    <article class="product" style="left:422px;width:140px">
      <p>orem ipsum dolor sit<br>amet, consectetur<br>adipiscing elit. Sed<br>$45.00</p>
      <div class="product-photo" role="img" aria-label="Home sweet home pink tapestry cushion" style="background:linear-gradient(135deg,#f1e4e6,#c98a98)"></div>
    </article>
    <article class="product" style="left:567px;width:135px">
      <p>orem ipsum dolor sit<br>amet, consectetur<br>adipiscing elit. Sed<br>$45.00</p>
      <div class="product-photo" role="img" aria-label="Cockerel tapestry cushion with black pompom trim" style="background:linear-gradient(135deg,#d8c9a4,#4a3b2c)"></div>
    </article>
    <article class="product" style="left:706px;width:142px">
      <p style="margin-top:5px">orem ipsum dolor sit<br>amet, consectetur<br>adipiscing elit. Sed<br>$45.00</p>
      <div class="best-seller">
        <svg width="11" height="11" viewBox="0 0 12 12" aria-hidden="true"><path d="M6 11 L1.2 5.6 A2.8 2.8 0 0 1 6 2.4 A2.8 2.8 0 0 1 10.8 5.6 Z" fill="#9b1111"/></svg>
        BEST SELLER
      </div>
      <div class="product-photo" role="img" aria-label="Union flag tapestry cushion" style="left:22px;top:79px;width:98px;background:linear-gradient(135deg,#9aa6c0,#7a2a3a)"></div>
    </article>
  </section>

  <footer class="footer">Needlecraftparcel 2012</footer>
</div>
</body>
</html>
```